Stationary package for Interior and construction company
Velvet Arch Studios
Professional
Peter Hallsey
Project Manager
Warehouse K42, Dubai Logistics Park Dubai,UAE PO Box 316052
velvetarchdxb@examplemail.test
www.velvetarchdubai.example
We require two business cards with different peoples names. #1 been Peter Hallsey the second persons details are. Simon Ravenholt, Project Manager, Warehouse K42, Dubai Logistics Park, Dubai, UAE, PO Box 316052, Cell- +971 50 6185072 Ph- +971 4 3061825 Email - s.ravenholt@velvetarchstudios.example Web - www.velvetarchstudios.example Brief, Velvet Arch Studios (VAS) is a luxury fit out and renovations company based in Dubai, UAE. VAS’s clientele are high net worth individuals. The company is looking for a suite of stationary to support their everyday business needs; this should include: • Letterheads (page 1 and page2) • Business cards (Two people) • Envelopes (A4, DL) • Notepad (A4, A5) The company would like to evoke a premium brand through chic, clean and sophisticated stationary items. Colour should not be over-used unnecessarily and the typeface should be clear to read. All artwork provided should be re-writable.
Please just use the logo, add the website to the bottom footer. open to options on layout and design.

```html
<!DOCTYPE html>
<html lang="en">
<head>
<meta charset="utf-8">
<title>Velvet Arch Studios – Business Cards</title>
<link href="https://fonts.googleapis.com/css2?family=Montserrat:wght@500;600&family=Open+Sans:wght@400;600&display=swap" rel="stylesheet">
<style>
  :root {
    --backdrop: #e4e6e8;
    --card: #ffffff;
    --brand-blue: #1e8fcf;
    --brand-grey: #8c9094;
    --text-dark: #4a4d50;
    --text-light: #ffffff;
  }
  * { margin: 0; padding: 0; box-sizing: border-box; }
  html, body { width: 1200px; height: 878px; overflow: hidden; }
  body {
    background: var(--backdrop);
    position: relative;
    font-family: "Open Sans", sans-serif;
  }
  .card {
    position: absolute;
    width: 540px;
    height: 310px;
    background: var(--card);
    box-shadow: 0 6px 18px rgba(0,0,0,0.18);
    overflow: hidden;
  }
  .card--front { left: 40px; top: 284px; }
  .card--back { left: 620px; top: 284px; }

  .brand {
    display: flex;
    align-items: center;
    gap: 12px;
  }
  .brand__dot {
    width: 44px; height: 44px;
    border-radius: 50%;
    background: var(--brand-blue);
    flex: none;
  }
  .brand__name {
    font-family: "Montserrat", sans-serif;
    font-weight: 600;
    color: var(--brand-blue);
    font-size: 21px;
    letter-spacing: 1px;
    line-height: 1.1;
    text-transform: uppercase;
  }
  .card--front .brand { position: absolute; left: 30px; top: 56px; z-index: 2; }
  .card--back .brand {
    position: absolute; left: 50%; top: 50%;
    transform: translate(-50%, -50%);
  }

  .contact {
    position: absolute;
    left: 292px;
    top: 76px;
    width: 236px;
    color: var(--text-dark);
    z-index: 2;
  }
  .contact__name {
    font-family: "Montserrat", sans-serif;
    font-weight: 600;
    font-size: 17px;
    line-height: 1.3;
    color: var(--brand-blue);
  }
  .contact__title {
    font-size: 11px;
    margin-bottom: 8px;
  }
  .contact__list { list-style: none; font-size: 10px; line-height: 1.5; }
  .contact__list li { display: flex; align-items: flex-start; gap: 6px; }
  .contact__list svg { width: 10px; height: 10px; flex: none; margin-top: 3px; fill: var(--brand-blue); }

  .footer-wave { position: absolute; left: 0; top: 0; width: 540px; height: 310px; z-index: 1; }
  .footer-wave .wave-grey { fill: var(--brand-grey); }
  .footer-wave .wave-blue { fill: var(--brand-blue); }
  .website {
    position: absolute;
    left: 30px;
    bottom: 22px;
    font-size: 11px;
    letter-spacing: 0.5px;
    color: var(--text-light);
    z-index: 2;
  }
</style>
</head>
<body>

  <section class="card card--front" aria-label="Business card front">
    <div class="brand">
      <span class="brand__dot"></span>
      <span class="brand__name">Velvet Arch<br>Studios</span>
    </div>

    <div class="contact">
      <p class="contact__name">Peter Hallsey</p>
      <p class="contact__title">Project Manager</p>
      <ul class="contact__list">
        <li><svg viewBox="0 0 10 10"><path d="M5 0a3.5 3.5 0 0 0-3.5 3.5C1.5 6 5 10 5 10s3.5-4 3.5-6.5A3.5 3.5 0 0 0 5 0zm0 5a1.5 1.5 0 1 1 0-3 1.5 1.5 0 0 1 0 3z"/></svg><span>Warehouse K42, Dubai Logistics Park<br>Dubai,UAE PO Box 316052</span></li>
        <li><svg viewBox="0 0 10 10"><path d="M2 0h2l1 2.5-1.3 1a6 6 0 0 0 2.8 2.8l1-1.3L10 6v2a2 2 0 0 1-2 2A8 8 0 0 1 0 2a2 2 0 0 1 2-2z"/></svg><span>+ 123 456 7890</span></li>
        <li><svg viewBox="0 0 10 10"><rect x="2" y="0" width="6" height="10" rx="1"/></svg><span>+ 123 456 7890</span></li>
        <li><svg viewBox="0 0 10 10"><rect x="0" y="3" width="10" height="5"/><rect x="2" y="0" width="6" height="3"/></svg><span>+ 123 456 7890</span></li>
        <li><svg viewBox="0 0 10 10"><path d="M0 2h10v6H0zM0 2l5 3.5L10 2"/></svg><span>velvetarchdxb@examplemail.test</span></li>
        <li><svg viewBox="0 0 10 10"><circle cx="5" cy="5" r="5"/></svg><span>www.velvetarchdubai.example</span></li>
      </ul>
    </div>

    <svg class="footer-wave" viewBox="0 0 540 310" aria-hidden="true">
      <path class="wave-grey" d="M0 178 C150 218 330 276 540 286 L540 300 C330 290 150 236 0 196 Z"/>
      <path class="wave-blue" d="M0 196 C150 236 330 290 540 300 L540 310 L0 310 Z"/>
    </svg>
    <p class="website">www.velvetarchdubai.example</p>
  </section>

  <section class="card card--back" aria-label="Business card back">
    <div class="brand">
      <span class="brand__dot"></span>
      <span class="brand__name">Velvet Arch<br>Studios</span>
    </div>
  </section>

</body>
</html>
```